Pelton|Marsh & Quillan business card contest

We need a logo for an upscale boutique diversified company involved in real estate, investments, cattle, and more. Our businesses DO NOT need to be reflected in the business card nor do we want them noted. This is our logo and colors and we love our logo and colors. Our logo looks best against a black background and we like to include the firm name in our logo usage. importantly, the names Pelton and Marsh are separated by | not / and we use an ampersand not the word and.
On the front of the card, we want to include:
company logo and name (Pelton|Marsh & Quillan)
on the back, we would definitely include:
address, email, cell #
logo and name (smaller size than front)

The variable will be location of individual name and title (mine for example is ) - whether on the front OR on the back. interested in variations from which to choose
Dr. Neil R. Whitcombe, CFA
Scientifique des Fusées Financières

we would like to use contemporary symbols for address, email address, cell # with an option for web site that we do not intend to use initially. we like two sided cards and believe this design should use four rounded corners with the standard size. we prefer thicker card stock and may look at metal.

```html
<!DOCTYPE html>
<html lang="en">
<head>
<meta charset="utf-8">
<title>Pelton|Marsh &amp; Quillan — Business Card</title>
<link rel="stylesheet" href="https://fonts.googleapis.com/css2?family=Lato:wght@400;700&display=swap">
<style>
  :root {
    --stage: #2b2b2b;
    --orange: #e07a1c;
    --orange-deep: #c9660f;
    --card-black: #121212;
    --white: #ffffff;
    --grey-mark: #9a9a9a;
    --grey-text: #6f6f6f;
  }
  * { box-sizing: border-box; margin: 0; padding: 0; }
  html, body {
    width: 1200px; height: 997px; overflow: hidden;
    background: var(--stage);
    font-family: "Lato", sans-serif;
  }
  .stage {
    width: 1200px; height: 997px;
    display: flex; flex-direction: column;
    align-items: center; justify-content: center; gap: 60px;
  }
  .card {
    width: 700px; height: 400px;
    border-radius: 26px;
    position: relative;
    overflow: hidden;
  }
  /* Front */
  .card--front {
    background: linear-gradient(135deg, var(--orange) 0%, var(--orange-deep) 100%);
    display: flex; align-items: center; justify-content: center;
  }
  .brand { display: flex; align-items: center; gap: 16px; }
  .brand__square { display: block; }
  .brand__name { font-weight: 400; white-space: nowrap; }
  .card--front .brand__square { width: 40px; height: 40px; background: var(--white); }
  .card--front .brand__name { font-size: 40px; color: var(--white); letter-spacing: 0.5px; }

  /* Back */
  .card--back { background: var(--card-black); }
  .card--back .brand { position: absolute; top: 58px; right: 56px; gap: 12px; }
  .card--back .brand__square { width: 22px; height: 22px; background: var(--orange); }
  .card--back .brand__name { font-size: 22px; color: var(--grey-mark); }

  .rule { position: absolute; height: 2px; background: var(--orange); }
  .rule--main { left: 40px; right: 40px; top: 196px; }
  .rule--short { left: 40px; width: 210px; top: 275px; height: 1.5px; }

  .person { position: absolute; left: 40px; top: 216px; }
  .person__name { color: var(--orange); font-size: 17px; font-weight: 400; }
  .person__title { color: var(--grey-text); font-size: 13px; margin-top: 6px; }

  .office { position: absolute; right: 40px; top: 216px; text-align: right; }
  .office__name { color: var(--orange); font-size: 16px; }
  .office__address { color: var(--grey-text); font-size: 13px; margin-top: 6px; }

  .contacts { position: absolute; left: 40px; top: 292px; list-style: none; }
  .contacts li {
    display: flex; align-items: center; gap: 12px;
    color: var(--grey-text); font-size: 14px; height: 24px;
  }
  .contacts svg { width: 14px; height: 14px; fill: var(--orange); flex: none; }
</style>
</head>
<body>
<main class="stage">
  <section class="card card--front" aria-label="Card front">
    <div class="brand">
      <span class="brand__square"></span>
      <span class="brand__name">Pelton|Marsh &amp; Quillan</span>
    </div>
  </section>

  <section class="card card--back" aria-label="Card back">
    <div class="brand">
      <span class="brand__square"></span>
      <span class="brand__name">Pelton|Marsh &amp; Quillan</span>
    </div>

    <div class="rule rule--main"></div>

    <div class="person">
      <p class="person__name">Maren Holt-Ashby</p>
      <p class="person__title">M.Ed., R.Psych.</p>
    </div>

    <div class="office">
      <p class="office__name">Pelton|Marsh &amp; Quillan</p>
      <p class="office__address">4127-48 St.Box 2210 Alder, AB T0X 9Z9</p>
    </div>

    <div class="rule rule--short"></div>

    <ul class="contacts">
      <li>
        <svg viewBox="0 0 16 16" aria-hidden="true"><path d="M3 1h3l1.5 4-2 1.3a9 9 0 0 0 4.2 4.2L11 8.5l4 1.5v3a2 2 0 0 1-2 2A12 12 0 0 1 1 3a2 2 0 0 1 2-2z"/></svg>
        403.555.0148
      </li>
      <li>
        <svg viewBox="0 0 16 16" aria-hidden="true"><path d="M1 3h14v10H1z M1 3l7 6 7-6" fill="none" stroke="#e07a1c" stroke-width="1.6"/><path d="M1 3h14L8 8.5z"/></svg>
        maren@ridgepsychology.ca
      </li>
      <li>
        <svg viewBox="0 0 16 16" aria-hidden="true"><circle cx="8" cy="8" r="6.5" fill="none" stroke="#e07a1c" stroke-width="1.5"/><path d="M1.5 8h13M8 1.5c-3 3.5-3 9.5 0 13M8 1.5c3 3.5 3 9.5 0 13" fill="none" stroke="#e07a1c" stroke-width="1.2"/></svg>
        www.ridgepsychology.ca
      </li>
    </ul>
  </section>
</main>
</body>
</html>
```